Swimming Pool Business Billboard

10' x 24' Billboard displaying company name, logo and phone number. Picture of swimming pool activity; kids playing , swimming, etc. Bullet points possibly shown: New Construction, Repairs, Weekly maintenance.

Industry/Entity Type

Swimming pool construction, repairs and maintenance.

Font styles to use
Sans Serif

Colors
0054AA
0677BA
7BADD7
CADEEF
E8F1F8

Requirements
Must have
• Benny & Carson Pelletier, BENNY'S POOLS & Service,
Nice to have
• Prefer to have my last name "Pelletier" above the word "POOLS" only in smaller print so that "BENNYS POOLS" is distinguished.

```html
<!DOCTYPE html>
<html lang="en">
<head>
<meta charset="utf-8">
<title>Benny's Pools &amp; Service Billboard</title>
<link href="https://fonts.googleapis.com/css2?family=Russo+One&family=Oswald:wght@600&family=Poppins:wght@500;700&family=Libre+Baskerville:ital,wght@1,700&display=swap" rel="stylesheet">
<style>
  :root {
    --navy: #0d2f5e;
    --pink: #e8137e;
    --yellow: #fcd20f;
    --white: #ffffff;
    --pool-light: #9fd9f2;
    --pool-mid: #4fb6e6;
    --pool-deep: #1f8fcf;
    --stage: #1c2b4d;
  }
  * { margin: 0; padding: 0; box-sizing: border-box; }
  html, body { width: 1200px; height: 822px; overflow: hidden; background: var(--stage); }
  .billboard {
    position: absolute; left: 0; top: 187px;
    width: 1200px; height: 447px;
    background: var(--white); overflow: hidden;
  }
  .billboard-shapes { position: absolute; inset: 0; }
  .owners {
    position: absolute; left: 110px; top: 46px;
    font-family: "Libre Baskerville", serif; font-style: italic; font-weight: 700;
    font-size: 33px; color: var(--navy); white-space: nowrap;
  }
  .brand-name {
    position: absolute; left: 47px; top: 96px;
    font-family: "Russo One", sans-serif; font-size: 84px; line-height: 1;
    letter-spacing: 4px; color: var(--pink); white-space: nowrap;
  }
  .brand-service {
    position: absolute; left: 116px; top: 190px;
    font-family: "Russo One", sans-serif; font-size: 84px; line-height: 1;
    letter-spacing: 2px; color: var(--navy); white-space: nowrap;
  }
  .logo-name {
    position: absolute; left: 80px; top: 335px; width: 126px;
    text-align: center; font-family: "Russo One", sans-serif;
    font-size: 20px; line-height: 1.1; color: var(--navy);
  }
  .call-label {
    position: absolute; left: 232px; top: 318px; width: 249px;
    text-align: center; font-family: "Poppins", sans-serif; font-weight: 500;
    font-size: 26px; color: var(--white);
  }
  .phone {
    position: absolute; left: 236px; top: 358px; width: 460px;
    text-align: center; font-family: "Poppins", sans-serif; font-weight: 700;
    font-size: 50px; line-height: 1; color: var(--white); letter-spacing: 1px;
  }
  .services {
    position: absolute; left: 696px; top: 352px; width: 504px;
    list-style: none; text-align: center;
    font-family: "Oswald", sans-serif; font-weight: 600; font-size: 27px;
    line-height: 36px; color: var(--navy);
  }
  .services li { display: inline-block; margin: 0 10px; }
  .services li::before { content: "• "; }
</style>
</head>
<body>
<main class="billboard">
  <svg class="billboard-shapes" width="1200" height="447" viewBox="0 0 1200 447">
    <defs>
      <linearGradient id="pool-water" x1="0" y1="0" x2="1" y2="1">
        <stop offset="0" stop-color="var(--pool-mid)"/>
        <stop offset="0.5" stop-color="var(--pool-light)"/>
        <stop offset="1" stop-color="var(--pool-deep)"/>
      </linearGradient>
    </defs>
    <g role="img" aria-label="Photo of two children playing on an inflatable ring in a blue swimming pool">
      <path d="M818 0 H1200 V346 H600 C640 300 700 280 760 220 C830 150 850 70 818 0 Z" fill="url(#pool-water)"/>
    </g>
    <path d="M796 0 C835 70 815 150 745 218 C690 272 640 300 585 346" fill="none" stroke="var(--yellow)" stroke-width="26"/>
    <path d="M836 0 C860 75 835 160 770 225 C715 280 660 300 640 346" fill="none" stroke="var(--white)" stroke-width="3"/>
    <rect x="696" y="344" width="504" height="103" fill="var(--yellow)"/>
    <path d="M0 370 Q0 346 24 346 H120 V447 H0 Z" fill="var(--pink)"/>
    <rect x="0" y="434" width="713" height="13" rx="6" fill="var(--navy)"/>
    <path d="M232 322 Q232 309 245 309 H469 Q481 309 481 322 V360 H232 Z" fill="var(--navy)"/>
    <circle cx="143" cy="362" r="80" fill="var(--navy)"/>
    <rect x="80" y="362" width="160" height="85" fill="var(--navy)"/>
    <circle cx="143" cy="364" r="63" fill="var(--white)"/>
    <rect x="236" y="348" width="460" height="86" rx="18" fill="var(--pink)"/>
  </svg>

  <p class="owners">Benny &amp; Carson Pelletier</p>
  <h1 class="brand-name">BENNYS POOLS</h1>
  <p class="brand-service">&amp; SERVICE</p>
  <p class="logo-name">BENNY'S POOLS</p>
  <p class="call-label">Call us now!</p>
  <p class="phone">912-555-0147</p>
  <ul class="services">
    <li>NEW CONSTRUCTION</li><li>REPAIRS</li><li>WEEKLY MAINTENANCE</li>
  </ul>
</main>
</body>
</html>
```